Consulting company requires a logo and business card design

I require a logo/business card design for a new company based in Sexsmith Alberta called TanRidge Field Advisory Ltd. I plan to provide the following services: Construction management/inspection for the oil and gas industry, as well as general consulting for Asset Management, fleet management, etc. Have attached a copy of resume for use as guide for

Target Market(s)

Businesses within the oil and gas production, construction and shipping industry

Industry/Entity Type

Oil And Gas

Contact Information for Business Card

Believe should highlight, services offered, safety, quality,

Logo Text

TanRidge Field Advisory (TRFA) ?

Font styles to use
Script

Requirements
Must have
• Open to all options

```html
<!DOCTYPE html>
<html lang="en">
<head>
<meta charset="utf-8">
<title>TanRidge Field Advisory Ltd. – Business Card</title>
<link rel="stylesheet" href="https://fonts.googleapis.com/css2?family=Noto+Serif:wght@400;700&display=swap">
<style>
  :root {
    --page-bg: #e9ecef;
    --blue-light: #1ea3d2;
    --blue-mid: #1f7fc4;
    --blue-deep: #1d4e9e;
    --paper: #f3f4f5;
    --paper-shade: #dcdfe2;
    --ink-blue: #1d6fb0;
    --white: #ffffff;
    --divider: #9aa4ad;
  }
  * { box-sizing: border-box; margin: 0; padding: 0; }
  html, body { width: 1200px; height: 780px; overflow: hidden; }
  body {
    background: var(--page-bg);
    font-family: "Noto Serif", Georgia, serif;
    position: relative;
  }
  .card {
    position: absolute;
    width: 520px;
    height: 297px;
    border-radius: 3px;
    overflow: hidden;
    box-shadow: 0 2px 0 #5d8fcf, 0 4px 0 #2b5fa8, 0 14px 30px rgba(0,0,0,0.25);
  }

  /* Back side: services */
  .card-back {
    left: 50px;
    top: 240px;
    background: radial-gradient(ellipse at 35% 30%, var(--blue-light) 0%, var(--blue-mid) 50%, var(--blue-deep) 100%);
    color: var(--white);
    text-align: center;
  }
  .card-back .brand-name {
    margin-top: 58px;
    font-size: 28px;
    font-weight: 400;
    letter-spacing: 0.5px;
  }
  .card-back .section-title {
    margin-top: 34px;
    font-size: 17px;
    font-weight: 700;
    letter-spacing: 0.5px;
  }
  .card-back .services {
    margin-top: 12px;
    font-size: 12.5px;
    line-height: 1.6;
  }

  /* Front side: contact */
  .card-front {
    left: 630px;
    top: 240px;
    background: linear-gradient(160deg, var(--white) 0%, var(--paper) 60%, var(--paper-shade) 100%);
  }
  .logo-area {
    height: 132px;
    display: flex;
    align-items: center;
    justify-content: center;
    gap: 12px;
    border-bottom: 2px solid var(--divider);
  }
  .logo-dot {
    width: 22px;
    height: 22px;
    border-radius: 50%;
    background: var(--ink-blue);
  }
  .logo-name {
    color: var(--ink-blue);
    font-size: 22px;
    font-weight: 400;
  }
  .contact-band {
    height: 165px;
    background: linear-gradient(120deg, var(--blue-light) 0%, var(--blue-mid) 45%, var(--blue-deep) 100%);
    color: var(--white);
    padding: 22px 0 0 40px;
  }
  .person-name {
    font-size: 17px;
    font-weight: 400;
    letter-spacing: 1px;
    text-transform: uppercase;
    margin-bottom: 14px;
  }
  .contact-line {
    font-size: 13px;
    font-weight: 700;
    line-height: 1.45;
    display: flex;
    align-items: center;
    gap: 6px;
  }
  .contact-icon { width: 14px; height: 14px; flex: none; }
</style>
</head>
<body>

  <section class="card card-back">
    <h1 class="brand-name">TanRidge Field Advisory Ltd.</h1>
    <h2 class="section-title">CORE COMPETENCIES</h2>
    <p class="services">
      Asset management | Strategic Planning | Process Improvement<br>
      Budget Planning &amp; Cost Control | Client Relations | Quality Control<br>
      Fleet Management | Construction Quality Management
    </p>
  </section>

  <section class="card card-front">
    <div class="logo-area">
      <span class="logo-dot"></span>
      <span class="logo-name">TanRidge Field Advisory Ltd.</span>
    </div>
    <div class="contact-band">
      <p class="person-name">Daniel Marsh</p>
      <p class="contact-line">RR#4 Ridgeview Alberta,</p>
      <p class="contact-line">T0K 2L0</p>
      <p class="contact-line">
        <svg class="contact-icon" viewBox="0 0 14 14" aria-hidden="true">
          <rect x="0.5" y="0.5" width="13" height="13" rx="2" fill="#fff"/>
          <path d="M4 3h2l1 2.5-1.2 1a6 6 0 0 0 1.8 1.8l1-1.2L11 8v2a1 1 0 0 1-1 1A7 7 0 0 1 3 4a1 1 0 0 1 1-1z" fill="#1f7fc4"/>
        </svg>
        (555)204-7719
      </p>
      <p class="contact-line">
        <svg class="contact-icon" viewBox="0 0 14 14" aria-hidden="true">
          <rect x="0.5" y="0.5" width="13" height="13" rx="2" fill="#fff"/>
          <rect x="2.5" y="4" width="9" height="6.5" fill="none" stroke="#1f7fc4" stroke-width="1.1"/>
          <path d="M2.5 4 7 7.8 11.5 4" fill="none" stroke="#1f7fc4" stroke-width="1.1"/>
        </svg>
        danielmarsh@example.com
      </p>
    </div>
  </section>

</body>
</html>
```